Förderverein einer Kirchengemeinde sucht Flyer-Design
Zielgruppe
Wir sind ein Förderverein einer Kirchengemeinde, der sich für die kirchenmusikalische Arbeit einsetzt.
Wir wünschen uns ein niveauvolles und zeitgemäßes/modernes Flyerdesign, das die etablierten Konzertbesucher anspricht, aber vor allem auch Menschen erreicht und überzeugt, die (noch) nichts mit Kirche zu tun haben.
Das Alter der (Haupt-) Zielgruppe (Männer und Frauen) erstreckt sich von 45 bis 70 Jahren.
Aufgabenstellung
Bei der Wahl des Formates würden wir (aus der Sicht von Laien) ein zweimal gefaltetes DIN A4 quer Format nehmen. Aber wir lassen uns gerne überraschen und sind grundsätzlich für andere Lösungen offen.
Bitte den Abschnitt für Adress- und sonstige Dateneintragungen samt Kontodaten so gestalten und platzieren, dass man ihn leicht abtrennen und verschicken kann.
Der Flyer soll Kirchenmusik als lebendig und attraktiv darstellen und neue (jüngere) Mitglieder für den Freundeskreis werben.
Lassen Sie die Bilder sprechen!!

```html
<!DOCTYPE html>
<html lang="de">
<head>
<meta charset="utf-8">
<title>Mitglieder haben gute Gründe</title>
<link rel="stylesheet" href="https://fonts.googleapis.com/css2?family=Nunito+Sans:wght@300;400;700&display=swap">
<style>
  :root {
    --red-dark: #9b1517;
    --red-light: #bd1a1d;
    --text-light: #ffffff;
  }
  html, body {
    margin: 0;
    padding: 0;
    width: 1200px;
    height: 846px;
    overflow: hidden;
    background: #ffffff;
  }
  .flyer-panel {
    position: relative;
    width: 1200px;
    height: 846px;
    overflow: hidden;
    font-family: "Nunito Sans", "Avenir Next", sans-serif;
  }
  .panel-art {
    position: absolute;
    inset: 0;
    width: 1200px;
    height: 846px;
  }
  .reasons-title {
    position: absolute;
    left: 601px;
    top: 100px;
    margin: 0;
    font-size: 28px;
    font-weight: 700;
    color: var(--text-light);
    letter-spacing: 0.01em;
    white-space: nowrap;
  }
  .reason-line {
    position: absolute;
    margin: 0;
    font-size: 19.5px;
    font-weight: 300;
    color: var(--text-light);
    letter-spacing: 0.045em;
    white-space: nowrap;
    line-height: 1;
  }
</style>
</head>
<body>
<main class="flyer-panel">
  <svg class="panel-art" viewBox="0 0 1200 846" xmlns="http://www.w3.org/2000/svg">
    <defs>
      <linearGradient id="brassPhoto" x1="0" y1="0" x2="0" y2="1">
        <stop offset="0" stop-color="#cfcbc1"/>
        <stop offset="0.18" stop-color="#e2e0da"/>
        <stop offset="0.38" stop-color="#eeede9"/>
        <stop offset="0.55" stop-color="#d9d3bf"/>
        <stop offset="0.7" stop-color="#5b5854"/>
        <stop offset="0.84" stop-color="#3c3a38"/>
        <stop offset="0.93" stop-color="#a8a49b"/>
        <stop offset="1" stop-color="#b9b5ad"/>
      </linearGradient>
      <linearGradient id="choirPhoto" x1="0" y1="0" x2="0" y2="1">
        <stop offset="0" stop-color="#d9b9a4"/>
        <stop offset="0.14" stop-color="#e3d6be"/>
        <stop offset="0.28" stop-color="#b9c2a6"/>
        <stop offset="0.42" stop-color="#c7b3a0"/>
        <stop offset="0.55" stop-color="#5a4f4a"/>
        <stop offset="0.7" stop-color="#2d2828"/>
        <stop offset="0.85" stop-color="#3a3331"/>
        <stop offset="1" stop-color="#1c1919"/>
      </linearGradient>
      <linearGradient id="redPanel" x1="0" y1="0" x2="1" y2="1">
        <stop offset="0" stop-color="var(--red-dark)"/>
        <stop offset="1" stop-color="var(--red-light)"/>
      </linearGradient>
    </defs>
    <rect class="photo-brass" x="0" y="0" width="640" height="423" fill="url(#brassPhoto)" role="img" aria-label="Foto: Posaunenchor in weißen Hemden und dunklen Hosen mit Trompeten, Posaunen und Tuben auf einer Treppe vor einem hellen Gebäude"/>
    <rect class="photo-choir" x="0" y="423" width="730" height="423" fill="url(#choirPhoto)" role="img" aria-label="Foto: Kirchenchor in Schwarz mit Notenmappen vor barockem Altarraum mit Säulen und Heiligenfiguren, Dirigent im Vordergrund"/>
    <polygon class="edge-band" points="520,0 540,0 735,846 715,846" fill="#ffffff" opacity="0.25"/>
    <polygon class="reasons-background" points="530,0 1200,0 1200,846 726,846" fill="url(#redPanel)"/>
  </svg>

  <h1 class="reasons-title">Mitglieder haben gute Gründe:</h1>

  <p class="reason-line" style="left:622px; top:182px;">Sie…</p>

  <p class="reason-line" style="left:632px; top:233px;">… erhalten ermäßigte Eintrittspreise von</p>
  <p class="reason-line" style="left:661px; top:261px;">gemeindeeigenen Konzerten</p>

  <p class="reason-line" style="left:655px; top:319px;">… können Konzertkarten vor dem öffentlichen</p>
  <p class="reason-line" style="left:682px; top:347px;">Verkauf erwerben</p>

  <p class="reason-line" style="left:674px; top:406px;">… gestalten die Arbeit des Freundeskreises</p>
  <p class="reason-line" style="left:705px; top:434px;">in den jährlichen Mitgliederversammlungen</p>
  <p class="reason-line" style="left:711px; top:462px;">aktiv mit</p>

  <p class="reason-line" style="left:703px; top:520px;">… erhalten aktuelle Informationen über</p>
  <p class="reason-line" style="left:733px; top:549px;">Veranstaltungen der Gemeinde bequem</p>
  <p class="reason-line" style="left:739px; top:577px;">per Email und profitieren so zu allererst</p>

  <p class="reason-line" style="left:730px; top:636px;">… können den Mitgliedsbeitrag steuerlich</p>
  <p class="reason-line" style="left:762px; top:664px;">absetzen und erhalten eine Spenden-</p>
  <p class="reason-line" style="left:767px; top:692px;">bescheinigung</p>
</main>
</body>
</html>
```